Business card design needed for Automotive Reconditioning business

I have a logo design i just cant decide on the best color or layout for the business card, I will upload all the files so you can see all colors schemes we are considering. I have other file formats if needed let me know.

Target Market(s)

automotive dealerships

Contact Information for Business Card

HERE are the Descriptions and info needed on the card:
Interior Repair: Leather carpet burns panels dash Deoderize
Dealer products and Vin Verify
( spot for name and cell number) My name is Dorian Pelk phone 951 430-2158 Title COO www.BrolvexMotor.com

Font styles to use
Sans Serif
Other font styles liked:
• what ever you think looks best

Requirements
Must have
• Must be able to change the name and phone for employees

```html
<!DOCTYPE html>
<html lang="en">
<head>
<meta charset="utf-8">
<title>Brolvex Auto Reconditioning Corp. – Business Card</title>
<link rel="stylesheet" href="https://fonts.googleapis.com/css2?family=Play:wght@400;700&family=Open+Sans:wght@400&display=swap">
<style>
  :root {
    --backdrop: #8c8c8c;
    --card-light: #ffffff;
    --card-dark: #1d1b1b;
    --brand-red: #c8202a;
    --ink-dark: #1a1a1a;
    --ink-light: #e4e4e4;
    --rule-light: #cfcfcf;
    --rule-dark: #5a5a5a;
  }
  * { margin: 0; padding: 0; box-sizing: border-box; }
  html, body {
    width: 1200px;
    height: 1200px;
    overflow: hidden;
    background: var(--backdrop);
  }
  .canvas {
    position: relative;
    width: 1200px;
    height: 1200px;
  }
  .card {
    position: absolute;
    top: 310px;
    height: 594px;
    text-align: center;
  }
  .card--front { left: 234px; width: 364px; background: var(--card-light); }
  .card--back  { left: 627px; width: 370px; background: var(--card-dark); }

  .brand-name {
    position: absolute;
    left: 0;
    right: 0;
    font-family: "Play", sans-serif;
    font-weight: 700;
    color: var(--brand-red);
    line-height: 1.15;
  }
  .brand-name__main { display: block; font-size: 40px; letter-spacing: 1px; }
  .brand-name__sub  { display: block; font-size: 15px; letter-spacing: 0.5px; }
  .card--front .brand-name { top: 168px; }
  .card--back  .brand-name { top: 232px; }

  .person {
    position: absolute;
    top: 396px;
    left: 0;
    right: 0;
    font-family: "Play", sans-serif;
  }
  .person__name {
    font-size: 25px;
    font-weight: 700;
    color: var(--brand-red);
    letter-spacing: 0.5px;
    line-height: 1;
  }
  .person__title {
    font-size: 17px;
    color: var(--ink-dark);
    margin-top: 4px;
    line-height: 1;
  }
  .rule {
    position: absolute;
    height: 1px;
  }
  .card--front .rule { top: 459px; left: 95px; width: 174px; background: var(--rule-light); }
  .card--back  .rule { top: 469px; left: 32px; width: 305px; background: var(--rule-dark); }

  .contact {
    position: absolute;
    top: 478px;
    left: 0;
    right: 0;
    font-family: "Play", sans-serif;
    font-size: 20px;
    color: var(--ink-dark);
    line-height: 32px;
  }
  .contact__label { color: var(--brand-red); }

  .services {
    position: absolute;
    top: 482px;
    left: 20px;
    right: 20px;
    font-family: "Open Sans", sans-serif;
    font-size: 17px;
    line-height: 21px;
    color: var(--ink-light);
  }
  .services__label { color: var(--brand-red); }
</style>
</head>
<body>
<main class="canvas">
  <section class="card card--front">
    <div class="brand-name">
      <span class="brand-name__main">BROLVEX</span>
      <span class="brand-name__sub">AUTO RECONDITIONING CORP.</span>
    </div>
    <div class="person">
      <p class="person__name">DORIAN PELK</p>
      <p class="person__title">CEO</p>
    </div>
    <div class="rule"></div>
    <div class="contact">
      <p><span class="contact__label">P:</span> 951 430-2158</p>
      <p><span class="contact__label">W:</span> www.BrolvexMotor.com</p>
    </div>
  </section>

  <section class="card card--back">
    <div class="brand-name">
      <span class="brand-name__main">BROLVEX</span>
      <span class="brand-name__sub">AUTO RECONDITIONING CORP.</span>
    </div>
    <div class="rule"></div>
    <p class="services"><span class="services__label">Interior Repair:</span> Leather carpet burns panels dash Deoderize Dealer products and Vin Verify</p>
  </section>
</main>
</body>
</html>
```